Looking for Landingpage / Website Designer

We are looking for a Web Designer / Developer for our upcoming Start Up Websites. The first project will be a simple responsive business website with a CTA- Button and an optional Newsletter Opt-In. We do aim for a modern online business approach, since we are a young company.

It is necessary to understand, that we need a conversion orientated design, not a wordpress blog with widgets and galleries.

We are currently discussing how it is going to happen and what preferences we need to focus on.

What we know is, that it should be more of a landing page with an option of adding 2 or 3 Navigation points.

We even thought about using services like plumvesta.com or crintofold.com to have an easier approach for future customizations and A/B testing.

We'd love to see how you fit the design/colors to the upcoming logo
(which is not the final version yet )

hope you can do something about that.

For the Structure.

1. Bracket

Slogan plus a preview text of what we are offering. On the right side a video placeholder plus CTA button.

2. Bracket

Illustrating 3 Benefits. On the right side - Opt in for Contact/Newsletter and CTA Button

3. Bracket

Picture with text just like you have it with the testimonial

You can orientate yourself towards to that landing page example as well:

http://cdn2.zorvellink.net/hub/53/file-581676469-png/Blog-Related_Images/plumvesta_landing_page.png?t=1416543075530

If our collaboration is going well, we would like to stay in touch for further projects.
Updates

Reason: There are 3 Design we do really like but, don't fit exactly our needs. 5 Days max.

Reason: For final adjustments.

I just uploaded the final logo :) Thank you for your commitment so far!

Target Market(s)

Our targeted audience could be almost everybody, who looks for an average paid side job (students, unemployed, house wives and whatever you can imagine). Maybe this is enough information for you to get a mere perception of what this is all about.

Industry/Entity Type

Business

Coding

Coded - Design and coding required

Font styles to use
Serif
Sans Serif

Colors
acd037
5c5c5c
33a6d7

Requirements
Must have
• Registration Opt-In
Responsive on any Device
Customizable
A benefits navigation just like in that example I've uploaded.
Nice to have
• As fast as possible ;D

```html
<!DOCTYPE html>
<html lang="en">
<head>
<meta charset="utf-8">
<title>Workvinta – Side Jobs</title>
<link href="https://fonts.googleapis.com/css2?family=Open+Sans:wght@300;400;600;700;800&display=swap" rel="stylesheet">
<style>
:root{
  --green:#55b947;
  --green-dark:#2f7a25;
  --green-deep:#1f5a18;
  --lime:#acd037;
  --blue:#33a6d7;
  --grey:#5c5c5c;
  --grey-light:#e6e6e6;
  --footer-bg:#ececec;
  --text:#333333;
  --white:#ffffff;
}
*{margin:0;padding:0;box-sizing:border-box}
html,body{width:1200px;height:2550px;overflow:hidden}
body{font-family:"Open Sans",Arial,sans-serif;color:var(--text);background:var(--white);position:relative}
.wrap{position:absolute;left:71px;width:1049px}

/* header */
.brand{display:flex;align-items:center;gap:8px;font-weight:700;color:var(--green);font-size:34px;letter-spacing:-0.5px}
.brand-dot{width:40px;height:40px;border-radius:50%;background:var(--green)}
.site-header{top:34px;height:50px;display:flex;justify-content:space-between;align-items:center}
.contact{display:flex;gap:22px;font-size:14px;color:var(--text)}
.contact span{display:flex;align-items:center;gap:8px}
.main-nav{top:99px;height:37px;background:var(--green);display:flex;align-items:center;border-bottom:2px solid var(--green-dark)}
.main-nav a{color:var(--white);text-decoration:none;font-size:13px;font-weight:700;padding:0 16px;height:100%;display:flex;align-items:center}
.main-nav a.active{background:var(--green-deep)}
.main-nav .search{margin-left:auto;gap:8px}

/* hero */
.slider-dots{position:absolute;top:158px;left:1018px;display:flex;gap:8px}
.slider-dots i{width:11px;height:11px;border-radius:50%;background:#cfcfcf}
.slider-dots i:first-child{background:var(--green)}
.hero-title{position:absolute;top:186px;left:0;width:1200px;text-align:center;font-size:41px;font-weight:800;color:var(--green);letter-spacing:0.5px}
.hero-photo{position:absolute;top:247px;left:0;width:1200px;height:386px;background:linear-gradient(180deg,#f4f4f4 0%,#c9ced6 45%,#8a93a0 75%,#eeeeee 100%)}
.hero-arrow{position:absolute;top:352px;width:28px;height:28px;background:#222;display:flex;align-items:center;justify-content:center}
.hero-form{position:absolute;top:498px;left:325px;display:flex;height:60px}
.hero-form .field{width:288px;background:var(--white);font-size:24px;color:#8a8a8a;display:flex;align-items:center;padding-left:16px}
.hero-form .btn{width:245px;background:var(--green-dark);color:var(--white);font-size:36px;font-weight:800;display:flex;align-items:center;justify-content:center}
.hero-rule{position:absolute;top:633px;left:0;width:1200px;height:3px;background:var(--green-dark)}

/* benefits */
.benefits{top:638px;height:314px;background:var(--green);display:flex;justify-content:space-around;padding:58px 70px 0}
.benefit{width:260px;text-align:center;color:var(--white)}
.benefit-icon{width:122px;height:122px;border-radius:50%;background:var(--white);margin:0 auto 30px;display:flex;align-items:center;justify-content:center}
.benefit h3{font-size:19px;font-weight:600;line-height:30px}
.benefit small{display:block;font-size:13px;line-height:14px}
.benefits-corner{position:absolute;right:0;bottom:0;width:0;height:0;border-left:38px solid transparent;border-bottom:38px solid var(--green-dark)}

/* student */
.student{top:952px;height:333px;display:flex}
.student-text{width:551px;background:var(--grey-light);padding:28px 44px}
h2{font-weight:300;font-size:34px;line-height:40px;color:#333}
.body-copy{font-size:13.5px;line-height:23.5px;margin-top:18px;color:#222}
.btn-blue{display:inline-block;margin-top:26px;background:var(--blue);color:var(--white);font-weight:700;font-size:21px;padding:6px 24px;box-shadow:2px 2px 0 rgba(0,0,0,.2)}
.video{flex:1;position:relative;background:linear-gradient(135deg,#7d94ad 0%,#b8c3cf 50%,#6b7f95 100%)}
.play{position:absolute;left:216px;top:140px;width:84px;height:58px;background:#e52420;border-radius:6px;display:flex;align-items:center;justify-content:center}

/* welcome */
.welcome{top:1285px;height:333px;display:flex}
.agent-photo{width:500px;background:linear-gradient(120deg,#e8e8ea 0%,#cfd2d6 60%,#f1f1f1 100%)}
.welcome-text{flex:1;background:var(--lime);padding:36px 36px}
.welcome-text h2{font-size:40px;color:#1d1d1d}
.welcome-text .body-copy{margin-top:20px;color:#1d1d1d}
.btn-dark{display:inline-block;margin-top:22px;background:var(--green-deep);color:var(--white);font-weight:700;font-size:21px;padding:6px 24px;box-shadow:2px 2px 0 rgba(0,0,0,.2)}

/* product */
.product{top:1618px;height:371px}
.product-text{position:absolute;left:43px;top:38px;width:620px}
.product-text h2{font-size:35px;line-height:42px}
.product-box{position:absolute;left:660px;top:38px;width:330px;height:320px;background:linear-gradient(135deg,#eef5ec 0%,#5cae4a 55%,#2f7a25 100%)}

/* newsletter */
.newsletter{top:1989px;height:175px;background:var(--grey);color:var(--white);padding:0 44px;display:flex;align-items:center}
.newsletter h2{color:var(--white);font-size:36px;line-height:40px;width:235px}
.nl-field{margin-right:22px}
.nl-field label{display:block;font-size:14px;margin-bottom:6px}
.nl-field span{display:block;width:252px;height:36px;background:var(--white)}
.nl-btn{margin-top:22px;background:var(--blue);color:var(--white);font-weight:700;font-size:21px;width:184px;height:36px;display:flex;align-items:center;justify-content:center;box-shadow:2px 2px 0 rgba(0,0,0,.25)}

/* footer */
.site-footer{position:absolute;top:2215px;left:0;width:1200px;height:247px;background:var(--footer-bg);border-top:3px solid var(--green-dark)}
.footer-brand{position:absolute;left:71px;top:44px;font-size:32px}
.footer-brand .brand-dot{width:38px;height:38px}
.address{position:absolute;left:86px;top:100px;font-size:13px;line-height:21px;color:#222}
.footer-col{position:absolute;top:40px}
.footer-col h4{font-weight:400;color:var(--green);font-size:19px;margin-bottom:10px}
.footer-nav li{list-style:none;font-size:13.5px;line-height:24px;color:#444;display:flex;align-items:center;gap:12px}
.footer-nav li::before{content:"";width:5px;height:5px;background:#aaa}
.footer-nav li:first-child::before{background:var(--green)}
.map{width:380px;height:148px;background:linear-gradient(135deg,#d9dccf 0%,#c9d2b8 50%,#dcd6c4 100%);border:1px solid #bbb}
.bottom-bar{position:absolute;top:2462px;left:0;width:1200px;height:88px;background:var(--grey);color:var(--white);font-size:13.5px}
.bottom-bar .copy{position:absolute;left:71px;top:36px}
.legal{position:absolute;right:80px;top:36px;display:flex;gap:28px}
</style>
</head>
<body>

<header class="wrap site-header">
  <div class="brand"><span class="brand-dot"></span>Workvinta</div>
  <div class="contact">
    <span><svg width="16" height="12" viewBox="0 0 16 12"><rect width="16" height="12" fill="#2f7a25"/><path d="M0 0 L8 7 L16 0" stroke="#fff" stroke-width="1.5" fill="none"/></svg>moreinfo@workvinta.de</span>
    <span><svg width="14" height="14" viewBox="0 0 24 24"><path fill="#2f7a25" d="M6.6 10.8c1.4 2.8 3.8 5.1 6.6 6.6l2.2-2.2c.3-.3.7-.4 1-.2 1.1.4 2.3.6 3.6.6.6 0 1 .4 1 1V20c0 .6-.4 1-1 1C10.6 21 3 13.4 3 4c0-.6.4-1 1-1h3.5c.6 0 1 .4 1 1 0 1.3.2 2.5.6 3.6.1.3 0 .7-.2 1z"/></svg>+68 254 71903</span>
  </div>
</header>

<nav class="wrap main-nav">
  <a class="active">HOME</a><a>GET HIRED</a><a>ABOUT US</a><a>OUR SERVICES</a><a>OUR BENEFITS</a><a>CONTACT US</a>
  <a class="search">SEARCH <svg width="16" height="16" viewBox="0 0 16 16"><circle cx="6.5" cy="6.5" r="5" stroke="#fff" stroke-width="2" fill="none"/><path d="M10.5 10.5 L15 15" stroke="#fff" stroke-width="2"/></svg></a>
</nav>

<div class="slider-dots"><i></i><i></i><i></i><i></i></div>
<h1 class="hero-title">LOOKING FOR AN AVERAGE PAID SIDE JOB</h1>
<div class="hero-photo" role="img" aria-label="Large group of smiling business people standing together"></div>
<div class="hero-arrow" style="left:75px"><svg width="10" height="14" viewBox="0 0 10 14"><path d="M8 1 L2 7 L8 13" stroke="#fff" stroke-width="2" fill="none"/></svg></div>
<div class="hero-arrow" style="left:1095px"><svg width="10" height="14" viewBox="0 0 10 14"><path d="M2 1 L8 7 L2 13" stroke="#fff" stroke-width="2" fill="none"/></svg></div>
<div class="hero-form"><div class="field">Email</div><div class="btn">SUBSCRIBE</div></div>
<div class="hero-rule"></div>

<section class="wrap benefits">
  <div class="benefit">
    <div class="benefit-icon"><svg width="40" height="44" viewBox="0 0 40 44"><path d="M4 2 H28 L36 10 V42 H4 Z" fill="#555"/><rect x="11" y="18" width="18" height="16" fill="#fff"/><rect x="14" y="6" width="3" height="8" fill="#fff"/><rect x="20" y="6" width="3" height="8" fill="#fff"/></svg></div>
    <h3>Sim Card with all<br>Net Flat for Private Use</h3>
  </div>
  <div class="benefit">
    <div class="benefit-icon"><svg width="50" height="36" viewBox="0 0 50 36"><rect width="50" height="36" fill="#555"/><g fill="#fff"><rect x="3" y="4" width="5" height="5"/><rect x="3" y="15" width="5" height="5"/><rect x="3" y="26" width="5" height="5"/><rect x="42" y="4" width="5" height="5"/><rect x="42" y="15" width="5" height="5"/><rect x="42" y="26" width="5" height="5"/><path d="M20 10 L32 18 L20 26 Z"/></g></svg></div>
    <h3>Free Distribution Training<br>Online with Videos</h3>
  </div>
  <div class="benefit">
    <div class="benefit-icon"><svg width="62" height="44" viewBox="0 0 62 44"><path d="M2 22 L24 2 L46 22 H40 V42 H8 V22 Z" fill="#555"/><circle cx="46" cy="24" r="7" fill="#555" stroke="#fff" stroke-width="2"/><path d="M34 44 C34 34 58 34 58 44 Z" fill="#555" stroke="#fff" stroke-width="2"/></svg></div>
    <h3>Homeoffice and Working<br>on Your Own Terms</h3>
    <small>(Time, Duration etc.)</small>
  </div>
  <span class="benefits-corner"></span>
</section>

<section class="wrap student">
  <div class="student-text">
    <h2>Are you a Student<br>and looking for a JOB</h2>
    <p class="body-copy">Lorem Ipsum is simply dummy text of the printing and typesetting industry. Lorem Ipsum has been the industry's standard dummy text ever since the 1500s, when an unknown printer took a galley of type and scrambled it to make a type specimen book.</p>
    <span class="btn-blue">SUBSCRIBE NEWS LETTER</span>
  </div>
  <div class="video" role="img" aria-label="Video preview of a young student holding folders on a city street">
    <div class="play"><svg width="22" height="24" viewBox="0 0 22 24"><path d="M0 0 L22 12 L0 24 Z" fill="#fff"/></svg></div>
  </div>
</section>

<section class="wrap welcome">
  <div class="agent-photo" role="img" aria-label="Smiling support agent wearing a headset"></div>
  <div class="welcome-text">
    <h2>Welcome to Workvinta.de</h2>
    <p class="body-copy">Lorem Ipsum is simply dummy text of the printing and typesetting industry. Lorem Ipsum has been the industry's standard dummy text ever since the 1500s, when an unknown printer took a galley of type and scrambled it to make a type specimen book. It has survived not only five centuries, but also the leap into electronic typesetting, remaining essentially unchanged. Lorem Ipsum is simply dummy text of the printing</p>
    <span class="btn-dark">READ MORE</span>
  </div>
</section>

<section class="wrap product">
  <div class="product-text">
    <h2>Lorem Ipsum is simply dummy text<br>of the printing and typesetting industry</h2>
    <p class="body-copy">Lorem Ipsum is simply dummy text of the printing and typesetting industry. Lorem Ipsum has been the industry's standard dummy text ever since the 1500s, when an unknown printer took a galley of type and scrambled it to make a type specimen book. It has survived not only five centuries, but also the leap into electronic typesetting, remaining essentially unchanged. Lorem Ipsum is simply dummy text of the printing</p>
  </div>
  <div class="product-box" role="img" aria-label="Green work box package with USB stick and SIM card"></div>
</section>

<section class="wrap newsletter">
  <h2>Subscribe Newsletter</h2>
  <div class="nl-field"><label>Name</label><span></span></div>
  <div class="nl-field"><label>Email</label><span></span></div>
  <div class="nl-btn">SUBSCRIBE</div>
</section>

<footer class="site-footer">
  <div class="brand footer-brand"><span class="brand-dot"></span>Workvinta</div>
  <p class="address">47 Larkwell Lane, Suite 8<br>Brindlemoor, VA 12455<br>Tel: (434) 555-0187</p>
  <div class="footer-col" style="left:541px">
    <h4>Navigations</h4>
    <ul class="footer-nav"><li>Home</li><li>Search jobs</li><li>Get hired</li><li>About us</li><li>Our services</li><li>Contact us</li></ul>
  </div>
  <div class="footer-col" style="left:736px">
    <h4>Our Location</h4>
    <div class="map" role="img" aria-label="Road map showing the office location"></div>
  </div>
</footer>

<div class="bottom-bar">
  <span class="copy">© 2014 workvinta.com - All Rights Reserved</span>
  <nav class="legal"><span>Sitemap</span><span>Legal Notice</span><span>Disclaimer</span><span>Privacy Policy</span></nav>
</div>

</body>
</html>
```